HML5 Web Application Design

We need a graphic design to give a HTML web application a modern look and feel. The design should be clean and neat with a metro inspired interface. All application uses vandrix controls so any experience with these would be great.
Perhaps you could also include a few screenshots of your previous work

Industry/Entity Type

Graphic Design

Requirements
Must have
• Must be HTML 5 compliant

```html
<!DOCTYPE html>
<html lang="en">
<head>
<meta charset="utf-8">
<title>Supplier Transaction Dashboard</title>
<link rel="stylesheet" href="https://fonts.googleapis.com/css2?family=Arimo:wght@400;700&family=Open+Sans:wght@300;400&display=swap">
<style>
:root{
  --page:#ffffff;
  --panel:#ececec;
  --header-top:#fbfbfb;
  --header-bottom:#d6d6d6;
  --header-line:#9a9a9a;
  --text:#222222;
  --table-head:#d9d9d9;
  --table-head-text:#555555;
  --table-line:#d0d0d0;
  --row-empty:#f4f4f4;
  --pager:#7aa822;
  --sky:#6bbce9;
  --ring-green:#79a83c;
  --ring-track:#f2f2f2;
  --caption:#a8a8a8;
  --badge:#d0161b;
  --icon:#7a7a7a;
  --row-1:#02a9c6;
  --row-2:#02b4d2;
  --row-3:#02c1df;
  --row-4:#0ccdeb;
  --row-5:#14dbfa;
  --divider:#ffffff;
}
*{box-sizing:border-box;margin:0;padding:0}
html,body{width:1200px;height:1030px;overflow:hidden;background:var(--page)}
.dashboard{position:absolute;left:0;top:0;width:1000px;height:858px;transform:scale(1.2);transform-origin:0 0;font-family:"Arimo",Arial,sans-serif;color:var(--text)}

.top-area{position:absolute;left:0;top:0;width:1000px;height:302px;background:var(--panel);border-bottom:1px solid #dcdcdc}
.app-header{position:absolute;left:0;top:0;width:1000px;height:73px;background:linear-gradient(var(--header-top),var(--header-bottom));border-bottom:2px solid var(--header-line)}
.logo-box{position:absolute;left:16px;top:8px;width:172px;height:56px;background:#fff;display:flex;align-items:center;justify-content:center;font-size:16px}
.main-nav{position:absolute;left:0;top:46px;width:1000px;height:18px;font-size:14px;line-height:16px}
.main-nav span{position:absolute;top:0;white-space:nowrap}
.header-tools{position:absolute;right:0;top:8px;width:150px;height:40px}

.screen-title{position:absolute;left:19px;top:94px;font-size:13px;white-space:nowrap}
.date-filter{position:absolute;top:118px;display:flex;align-items:center;font-size:13px;white-space:nowrap}
.date-filter .field{width:149px;height:25px;background:#fff;border:1px solid #d4d4d4;margin-left:6px;position:relative}
.date-filter .field svg{position:absolute;right:6px;top:6px}

.grid{position:absolute;left:20px;top:150px;width:963px;height:131px;background:#fff;border:1px solid var(--table-line);font-size:12px}
.grid-row{display:flex;border-bottom:1px solid var(--table-line)}
.grid-row div{border-right:1px solid var(--table-line);text-align:center;white-space:nowrap}
.grid-row div:last-child{border-right:none}
.grid-head{height:30px;background:var(--table-head);line-height:30px;font-weight:700;color:var(--table-head-text)}
.grid-empty{height:27px;background:var(--row-empty)}
.grid-data{height:44px}
.grid-data div{padding-top:5px}
.c1{width:158px}.c2{width:185px}.c3{width:264px}.c4{width:178px}.c5{width:178px}
.pager{position:absolute;left:408px;top:104px}
.pager-info{position:absolute;right:20px;top:110px;font-size:12px;white-space:nowrap}

.goals-card{position:absolute;left:17px;top:328px;width:422px;height:273px;background:var(--sky)}
.goals-card > svg{position:absolute;left:0;top:0}
.goals-title{position:absolute;left:0;width:100%;top:232px;display:flex;justify-content:center;align-items:center;gap:6px;white-space:nowrap;font-family:"Open Sans",sans-serif;font-weight:300;font-size:22px;line-height:28px;color:#fff}

.gauge{position:absolute;width:240px;text-align:center}
.gauge svg{display:block;margin:0 auto}
.gauge-value{position:absolute;left:0;width:100%;font-family:"Open Sans",sans-serif;font-weight:300;font-size:46px;color:#fff;white-space:nowrap}
.gauge-label{font-family:"Open Sans",sans-serif;font-weight:300;font-size:25px;color:var(--caption);white-space:nowrap}

.stats-list{position:absolute;left:20px;top:653px;width:963px;font-family:"Open Sans",sans-serif;font-weight:300;color:#fff;font-size:19px}
.stat-row{position:relative;height:38px;white-space:pre}
.stat-row span{position:absolute;top:0;line-height:38px}
.stat-row .toggle{left:0;width:36px;height:38px;border-right:1px solid var(--divider);text-align:center;font-size:26px;font-weight:400}
.stat-row .label{left:48px}
.r1{background:var(--row-1)}.r2{background:var(--row-2)}.r3{background:var(--row-3)}.r4{background:var(--row-4)}.r5{background:var(--row-5)}
</style>
</head>
<body>
<main class="dashboard">
  <section class="top-area">
    <header class="app-header">
      <div class="logo-box">Logo</div>
      <nav class="main-nav">
        <span style="left:238px">Home</span>
        <span style="left:306px">Pin Request</span>
        <span style="left:413px">Transaction</span>
        <span style="left:517px">Tax Details</span>
        <span style="left:617px">Users</span>
        <span style="left:684px">Suppliers</span>
        <span style="left:773px">Queries</span>
        <span style="left:853px">LA Staff</span>
        <span style="left:934px">Queries</span>
      </nav>
      <svg class="header-tools" viewBox="0 0 150 40" width="150" height="40" aria-hidden="true">
        <g fill="none" stroke="var(--icon)" stroke-width="2">
          <rect x="12" y="12" width="24" height="17"/>
          <path d="M12 12 L24 22 L36 12"/>
        </g>
        <circle cx="37" cy="9" r="8" fill="var(--badge)"/>
        <text x="37" y="12" font-size="9" fill="#fff" text-anchor="middle" font-family="Arimo,sans-serif">12</text>
        <g transform="translate(75,20)" fill="var(--icon)">
          <circle r="9"/>
          <g stroke="var(--icon)" stroke-width="4">
            <path d="M0 -13V13M-13 0H13M-9 -9L9 9M9 -9L-9 9"/>
          </g>
          <circle r="4" fill="#e6e6e6"/>
        </g>
        <g fill="none" stroke="var(--icon)" stroke-width="2.2" stroke-linecap="round">
          <path d="M114 12 A11 11 0 1 0 128 12"/>
          <path d="M121 6 V19"/>
        </g>
      </svg>
    </header>

    <div class="screen-title">Supplier Transaction Screen</div>
    <div class="date-filter" style="left:19px">Date From:<span class="field"><svg width="12" height="12" viewBox="0 0 12 12"><rect x="0.5" y="0.5" width="11" height="11" fill="none" stroke="#666"/><path d="M0 3H12M3 3V12M6 3V12M9 3V12M0 6H12M0 9H12" stroke="#666"/></svg></span></div>
    <div class="date-filter" style="left:250px">Date To:<span class="field"><svg width="12" height="12" viewBox="0 0 12 12"><rect x="0.5" y="0.5" width="11" height="11" fill="none" stroke="#666"/><path d="M0 3H12M3 3V12M6 3V12M9 3V12M0 6H12M0 9H12" stroke="#666"/></svg></span></div>

    <div class="grid">
      <div class="grid-row grid-head"><div class="c1">Date</div><div class="c2">Type</div><div class="c3">Reference</div><div class="c4">Amount</div><div class="c5">Status</div></div>
      <div class="grid-row grid-empty"><div class="c1"></div><div class="c2"></div><div class="c3"></div><div class="c4"></div><div class="c5"></div></div>
      <div class="grid-row grid-data"><div class="c1">01/01/2000</div><div class="c2">Inv</div><div class="c3">12345</div><div class="c4">100</div><div class="c5">Received</div></div>
      <svg class="pager" width="160" height="24" viewBox="0 0 160 24" aria-label="Pager">
        <g fill="var(--pager)">
          <circle cx="12" cy="12" r="11"/><circle cx="40" cy="12" r="11"/><circle cx="70" cy="12" r="11"/><circle cx="102" cy="12" r="11"/><circle cx="133" cy="12" r="11"/>
        </g>
        <g fill="none" stroke="#fff" stroke-width="2.4" stroke-linecap="round" stroke-linejoin="round">
          <path d="M11 7 L6 12 L11 17 M17 7 L12 12 L17 17"/>
          <path d="M43 7 L38 12 L43 17"/>
          <path d="M99 7 L104 12 L99 17"/>
          <path d="M127 7 L132 12 L127 17 M133 7 L138 12 L133 17"/>
        </g>
        <text x="70" y="16" font-size="11" fill="#fff" text-anchor="middle" font-family="Arimo,sans-serif">1</text>
      </svg>
      <div class="pager-info">1-2 of 2 items</div>
    </div>
  </section>

  <section class="goals-card">
    <svg width="422" height="273" viewBox="0 0 422 273" aria-label="Goals line chart">
      <polyline points="46,163 105,113 155,138 214,99 271,57 335,45 393,20" fill="none" stroke="#fff" stroke-width="3"/>
      <g fill="#fff">
        <circle cx="46" cy="163" r="5"/><circle cx="155" cy="138" r="5"/><circle cx="214" cy="99" r="5"/><circle cx="271" cy="57" r="6"/><circle cx="335" cy="45" r="6"/><circle cx="393" cy="20" r="6"/>
      </g>
      <circle cx="105" cy="113" r="7" fill="var(--sky)" stroke="#fff" stroke-width="2"/>
      <circle cx="105" cy="113" r="4" fill="#fff"/>
      <g fill="#fff" font-family="Open Sans,sans-serif" font-size="14" text-anchor="middle">
        <text x="48" y="186">10</text><text x="106" y="138">20</text><text x="155" y="162">15</text><text x="214" y="125">30</text><text x="279" y="83">30</text><text x="342" y="73">40</text><text x="397" y="49">50</text>
      </g>
    </svg>
    <div class="goals-title"><span>Your goals</span><svg width="16" height="13" viewBox="0 0 16 13" aria-hidden="true"><path d="M8 0 L16 13 H0Z" fill="#fff"/></svg></div>
  </section>

  <section class="gauge" style="left:460px;top:330px">
    <svg width="240" height="240" viewBox="0 0 240 240" aria-label="Active visitors 60 percent">
      <circle cx="120" cy="116" r="101" fill="none" stroke="var(--ring-track)" stroke-width="15"/>
      <circle cx="120" cy="116" r="101" fill="none" stroke="var(--ring-green)" stroke-width="15" stroke-dasharray="380.8 634.6" transform="translate(240,0) scale(-1,1) rotate(-90 120 116)"/>
      <circle cx="120" cy="116" r="68" fill="var(--sky)"/>
    </svg>
    <div class="gauge-value" style="top:86px">60%</div>
    <div class="gauge-label" style="margin-top:-12px">Active Visitors</div>
  </section>

  <section class="gauge" style="left:722px;top:328px">
    <svg width="240" height="240" viewBox="0 0 240 240" aria-label="Statistics visitors 70 percent">
      <circle cx="120" cy="116" r="101" fill="none" stroke="var(--ring-track)" stroke-width="15"/>
      <circle cx="120" cy="116" r="101" fill="none" stroke="var(--ring-green)" stroke-width="15" stroke-dasharray="444.2 634.6" transform="translate(240,0) scale(-1,1) rotate(-90 120 116)"/>
      <circle cx="120" cy="116" r="68" fill="var(--sky)"/>
    </svg>
    <div class="gauge-value" style="top:84px">70%</div>
    <div class="gauge-label" style="margin-top:-10px">Statistics (Visitors)</div>
  </section>

  <section class="stats-list">
    <div class="stat-row r1"><span class="toggle">+</span><span class="label">Top keywords :</span><span style="left:204px">Searchly  - 1050</span><span style="left:373px">Findo  - 124</span><span style="left:500px">Yodelo  - 984</span></div>
    <div class="stat-row r2"><span class="toggle">+</span><span class="label">Top Referrals :</span><span style="left:202px">Friendloop  - 300</span><span style="left:378px">Chirper   - 215</span><span style="left:528px">styleauthor.net   - 120</span></div>
    <div class="stat-row r3"><span class="toggle">+</span><span class="label">Top Social Traffic :</span><span style="left:237px">Friendloop  - 300</span><span style="left:413px">Chirper   - 215</span><span style="left:568px">Tumbleon  500</span><span style="left:719px">Circlo+  20</span></div>
    <div class="stat-row r4"><span class="toggle">+</span><span class="label">Top Active Pages :</span><span style="left:239px">-</span><span style="left:340px">-</span><span style="left:431px">-</span><span style="left:526px">-</span><span style="left:618px">-</span><span style="left:720px">-</span></div>
    <div class="stat-row r5"><span class="toggle">+</span><span class="label">Top Locations :</span><span style="left:210px">India - 1584</span><span style="left:358px">Canada  -  301</span><span style="left:532px">France  -  541</span><span style="left:685px">US  -  251</span></div>
  </section>
</main>
</body>
</html>
```